Bakery Business Cards

We are in need of business cards for our bakery business--something non-generic that reflects our business and will stand out. We are a wholesale bakery that primarily services in-store bakeries, casinos, schools, distributors, and fund-raising companies. The family business was founded in 1960. (www.marlowsovenworks.com)

```html
<!DOCTYPE html>
<html lang="en">
<head>
<meta charset="utf-8">
<title>Marlow's Ovenworks – Business Card</title>
<link href="https://fonts.googleapis.com/css2?family=Montserrat:wght@400;600;700&display=swap" rel="stylesheet">
<style>
  :root {
    --brand-blue: #2a4f9e;
    --paper-white: #ffffff;
    --backdrop: #a8a8a8;
  }
  * { box-sizing: border-box; margin: 0; padding: 0; }
  html, body {
    width: 900px; height: 1200px; overflow: hidden;
    background: var(--backdrop);
    font-family: 'Montserrat', Arial, sans-serif;
  }
  .canvas { position: relative; width: 900px; height: 1200px; }
  .card {
    position: absolute; left: 79px; width: 743px; height: 440px;
    background: var(--brand-blue); overflow: hidden;
  }
  .card--front { top: 129px; }
  .card--back { top: 638px; }
  .card__shape { position: absolute; inset: 0; }
  .contact {
    position: absolute; left: 60px; top: 124px; color: var(--paper-white);
  }
  .contact__name { font-size: 25px; font-weight: 700; line-height: 1.2; }
  .contact__role { font-size: 15px; font-weight: 400; margin-top: 4px; }
  .contact__address { font-size: 15.5px; line-height: 22px; margin-top: 42px; }
  .contact__list { list-style: none; margin-top: 28px; font-size: 15.5px; }
  .contact__list li { display: flex; align-items: center; height: 23px; }
  .contact__list svg { width: 14px; height: 14px; margin-right: 12px; fill: var(--paper-white); }
  .wordmark {
    position: absolute; text-align: center; font-weight: 700; line-height: 1.05;
  }
  .wordmark--front {
    left: 380px; width: 330px; top: 150px; font-size: 38px; color: var(--brand-blue);
  }
  .wordmark--back {
    left: 0; width: 743px; top: 150px; font-size: 60px; color: var(--paper-white);
  }
</style>
</head>
<body>
<main class="canvas">
  <section class="card card--front">
    <svg class="card__shape" viewBox="0 0 743 440" aria-hidden="true">
      <path d="M410 0 C330 120 360 330 478 440 L743 440 L743 0 Z" fill="var(--paper-white)"/>
      <path d="M362 140 C338 260 365 380 412 440 L424 440 C380 372 356 262 362 140 Z" fill="var(--paper-white)"/>
    </svg>
    <div class="contact">
      <h1 class="contact__name">Daniel Reyes</h1>
      <p class="contact__role">Operation Manager</p>
      <p class="contact__address">1875 Harmon Ave,<br>Tulsa Ridge, OK 74012</p>
      <ul class="contact__list">
        <li><svg viewBox="0 0 16 16"><path d="M3 2 L6 2 L7 5 L5.5 6.5 C6.5 8.5 7.5 9.5 9.5 10.5 L11 9 L14 10 L14 13 C14 14 13 14 12 14 C6 13.5 2.5 10 2 4 C2 3 2 2 3 2 Z"/></svg>(405) 555-0187</li>
        <li><svg viewBox="0 0 16 16"><path d="M1 3 H15 V13 H1 Z M1 3 L8 9 L15 3" stroke="var(--brand-blue)" stroke-width="1"/></svg>sales@marlowsovenworks.com</li>
        <li><svg viewBox="0 0 16 16"><circle cx="8" cy="8" r="7"/><path d="M4 5 C6 4 7 6 6 8 C5 10 7 11 7 13 M10 3 C9 5 11 6 12 8" stroke="var(--brand-blue)" stroke-width="1.2" fill="none"/></svg>www.marlowsovenworks.com</li>
      </ul>
    </div>
    <p class="wordmark wordmark--front">Marlow's<br>Ovenworks</p>
  </section>

  <section class="card card--back">
    <p class="wordmark wordmark--back">Marlow's<br>Ovenworks</p>
  </section>
</main>
</body>
</html>
```